Bref créative |
Martial Arts School Website | ||
Sports | ||
http://www.kovenbrightly.com | ||
We are a martial arts school. We are not a sport style school. We focus on street practical self defense. We have a range of students from 3 to 90 years old. | ||
Everyone seems to like my current site but I am looking for something possibly brighter. More up to tech. Social integration, blog etc. Also something that is unique. The one I built is based off of a template I found. | ||
Cutting-Edge Unique/Creative High Tech |
left side | ||
I am not sure how to define some of the questions. I don't want to put you in a box to much. Please see my current site. http://www.kovenbrightly.com I am not concerned about the navigation bars location .......I am almost thinking an icon based home page where they can click on the icon for the schedule, kids class information, school location, contact etc |
FMAFSLogo405dpi___Copy_36793.png This is my school Logo I designed several years ago. We will keep the design for our website and brochures, business cards etc. But I am looking for fresh contemporary up to date design and functionality for my site. Social integration etc. |
plovarek_gtrlb_site_logo_36794.png This is my school Logo I designed several years ago. We will keep the design for our website and brochures, business cards etc. But I am looking for fresh contemporary up to date design and functionality for my site. Social integration etc. |

```html
<!DOCTYPE html>
<html lang="en">
<head>
<meta charset="utf-8">
<title>Gateway Ridge Budo &amp; Fitness Studio</title>
<link rel="stylesheet" href="https://fonts.googleapis.com/css2?family=Arimo:wght@400;700&display=swap">
<style>
:root{
  --red:#c5192d;
  --red-dark:#8e0f1d;
  --red-deep:#5e0a14;
  --nav:#3a3a3a;
  --nav-dark:#222;
  --paper:#ffffff;
  --page:#e9e9e9;
  --ink:#555;
  --heading:#b01527;
  --side:#4a4a4a;
  --box-gray:#3f3f3f;
}
*{box-sizing:border-box;margin:0;padding:0}
html,body{width:1200px;height:976px;overflow:hidden}
body{position:relative;font-family:"Arimo",Arial,sans-serif;background:linear-gradient(#dcdcdc,#f4f4f4 60%,#e4e4e4);color:var(--ink)}
.header-band{position:absolute;left:0;top:0;width:1200px;height:300px;background:linear-gradient(90deg,var(--red-deep),var(--red) 25%,#d4374a 50%,var(--red) 75%,var(--red-deep));}
.topbar{position:absolute;left:0;top:0;width:1200px;height:40px;background:linear-gradient(var(--nav),var(--nav-dark))}
.nav{position:absolute;left:360px;top:8px;display:flex;gap:6px;list-style:none}
.nav li{height:26px;padding:0 14px;line-height:26px;font-size:11px;color:#fff;background:var(--red);border-radius:2px}
.nav li.current{background:#fff;color:var(--red)}
.brand{position:absolute;left:222px;top:14px;width:140px;text-align:center}
.brand-mark{width:110px;height:110px;margin:0 auto;border-radius:50%;background:#f2f2f2;border:4px solid #fff}
.brand-name{margin-top:-14px;background:#fff;border-radius:6px;padding:4px 6px;font-size:14px;font-weight:700;color:#333;line-height:1.15}
.verse{position:absolute;left:445px;top:56px;width:340px;height:76px;background:rgba(255,255,255,.85);text-align:center;font-size:13px;color:var(--red);padding-top:8px;line-height:1.3}
.shell{position:absolute;left:240px;top:162px;width:722px;height:748px;background:var(--paper);box-shadow:0 0 12px rgba(0,0,0,.3)}
.hero{position:absolute;left:20px;top:14px;width:682px;height:202px;border-radius:8px;background:linear-gradient(90deg,#2c2c2c,#8d8a86 30%,#d8d2cc 55%,#7a7570 80%,#2a2a2a)}
.sidebar{position:absolute;left:20px;top:224px;width:132px;height:514px;background:var(--side);padding:14px 10px}
.disc{width:100px;height:100px;margin:0 auto 10px;border-radius:50%;background:radial-gradient(#c98a4a,#6d3e1a)}
.badge{width:100px;height:100px;margin:0 auto 14px;border-radius:50%;background:#e4e4e4;border:6px solid var(--red-dark)}
.social{background:#fff;padding:6px;font-size:10px;color:#333;line-height:1.3}
.social-name{font-size:15px;font-weight:700;color:#3b5ea0;margin-bottom:4px}
.social-page{display:flex;gap:6px;align-items:center;margin-bottom:4px}
.social-page span.sq{width:30px;height:30px;background:#ddd;flex:none}
.content{position:absolute;left:160px;top:226px;width:542px}
.welcome{display:flex;align-items:center;gap:8px;font-size:15px;font-weight:700;color:var(--heading);text-transform:uppercase}
.welcome span.dot{width:28px;height:28px;border-radius:50%;background:#ddd;flex:none}
.body p{font-size:9px;line-height:1.35;margin-top:6px}
.cards{position:absolute;left:160px;top:472px;display:flex;gap:8px}
.card{width:176px;height:266px;color:#fff;font-size:9px;line-height:1.4;position:relative;border-radius:4px;overflow:hidden}
.card.gray{background:var(--box-gray)}
.card.red{background:linear-gradient(var(--red),var(--red-dark))}
.card h3{font-size:13px;padding:8px 10px;background:rgba(0,0,0,.25);font-weight:700}
.card p{padding:6px 10px}
.card .more{position:absolute;right:8px;bottom:8px;font-size:9px;font-weight:700;background:rgba(0,0,0,.3);padding:3px 8px}
</style>
</head>
<body>
<div class="header-band" role="img" aria-label="Red banner with faded photo of martial artists training"></div>
<div class="topbar"></div>
<ul class="nav">
  <li class="current">HOME</li><li>SCHEDULE</li><li>KIDS CLASS</li><li>SCHOOL LOCATION</li><li>OFFERS</li><li>CLASSES</li><li>CONTACT US</li>
</ul>
<div class="brand">
  <div class="brand-mark"></div>
  <div class="brand-name">Gateway Ridge Budo &amp; Fitness Studio</div>
</div>
<div class="verse">If Possible So Far<br>As it depends on you,<br>Live at peace with all men<br>Romans 12:18</div>

<main class="shell">
  <div class="hero" role="img" aria-label="Photo of a martial artist's arm and white uniform striking"></div>
  <aside class="sidebar">
    <div class="disc" role="img" aria-label="Training DVD cover"></div>
    <div class="badge" role="img" aria-label="Partner certification badge"></div>
    <div class="social">
      <div class="social-name">Friendwall</div>
      <div class="social-page"><span class="sq"></span><b>Gateway Ridge Budo</b></div>
      <div>Like</div>
      <div>Our studio will be closed Monday.</div>
    </div>
  </aside>
  <section class="content">
    <h1 class="welcome"><span class="dot"></span>Welcome Gateway Ridge Budo School</h1>
    <div class="body">
      <p>We are having a new look! If you have not been registered to our newsletter yet, invite your friends and join us for weekly updates. Our mat is open Monday through Saturday.</p>
      <p>Click on menu to see classes. Please feel free to leave a note if you are able.</p>
      <p>We are a Christ centered martial arts and self protection program.</p>
      <p>Street practical defense is what we teach here. Every student learns awareness, balance and control before speed. Our instructors work with children from three years old and adults well past ninety, so each class is shaped to the people on the mat. You will train hard, laugh often and leave stronger than you came.</p>
      <p>Please take time to look around. We believe a safe school builds strong families, and our doors are always open for a free trial lesson with a parent or friend.</p>
    </div>
  </section>
  <div class="cards">
    <article class="card gray"><h3>SCHOOL TUITION</h3><p>While we teach practical self defense, we keep our tuition simple and fair for every family.</p><p>Registration is one time fee. It includes the student uniform, belt and school patch.</p><p>Monthly Tuition $125 per month</p><span class="more">Add to Cart</span></article>
    <article class="card red"><h3>Current Specials</h3><p>Police officers, fire fighters and teachers train with a reduced fee this season. Bring a friend to any class in the month and both receive a free week. Ask at the front desk for details.</p><span class="more">Read More</span></article>
    <article class="card red"><h3>CHRIST FIRST</h3><p>We are a Christ centered school and we teach with patience and respect. We ask every student to treat others with kindness on and off the mat, and to use their skills only to protect.</p><span class="more">Read More</span></article>
  </div>
</main>
</body>
</html>
```